create a Wedding Invitation design

Personalized wedding invitation using names, initials, a nice monogram with decorative border

incorporate names: Lena and Osmond (first names)
Halvorsk (surname)
and wedding date , April 12, 2014

Colors: black ink on white;
optional accent colors: bright pink, bright orange, cajun red (may be flowers)
No shades of Purple

Industry/Entity Type

Wedding

Requirements
Must have
• Romantic, slightly formal looking design, black on white ; some accent color preferred, monogram (using first names Lena and Osmond and last name Halvorsk), that could be isolated and used on RSVP cards preferred
Nice to have
• idea of being at the top of a building (venue is called Brightmoor Hall) - the wedding is being held on the 17th floor of building with panoramic views of Washington DC and the mountains ; Washington DC skyline, iconic DC cherry blossoms

Here are some examples of a typical Washington, DC skyline (this is an optional or secondary feature only - not to dominate the design):
http://www.pictovane.com/clip-art/washington-dc.html#comp.asp?recid=48113760&xtra=
Cherry blossoms : http://www.jaunterly.com/news/story_8146.html

```html
<!DOCTYPE html>
<html lang="en">
<head>
<meta charset="utf-8">
<title>Lena &amp; Osmond — Wedding Invitation</title>
<link rel="stylesheet" href="https://fonts.googleapis.com/css2?family=Cinzel:wght@400;500&display=swap">
<style>
  :root {
    --paper: #ffffff;
    --ink: #141414;
    --frame: #c9c9c9;
    --ornament: #d9d9d9;
    --skyline: #111111;
  }
  html, body {
    margin: 0;
    padding: 0;
    background: var(--paper);
    overflow: hidden;
  }
  .invitation {
    position: relative;
    width: 862px;
    height: 1200px;
    background: var(--paper);
    overflow: hidden;
    font-family: "Cinzel", "Trajan Pro", serif;
    color: var(--ink);
  }
  .window {
    position: absolute;
    inset: 0;
    width: 862px;
    height: 1200px;
    display: block;
  }
  .window-frame { fill: var(--frame); fill-rule: evenodd; }
  .window-bar { stroke: var(--frame); stroke-width: 11; fill: none; }
  .monogram-ornament { fill: var(--ornament); }
  .monogram-plaque { fill: var(--paper); stroke: var(--ink); stroke-width: 1; }
  .skyline { fill: var(--skyline); }

  .monogram {
    position: absolute;
    left: 0;
    width: 862px;
    top: 60px;
    text-align: center;
    font-size: 40px;
    font-weight: 500;
    line-height: 1;
    letter-spacing: 0.02em;
  }
  .couple {
    position: absolute;
    left: 0;
    width: 862px;
    top: 364px;
    margin: 0;
    text-align: center;
    font-size: 38px;
    font-weight: 400;
    letter-spacing: 0.04em;
    line-height: 1;
  }
  .details {
    position: absolute;
    left: 0;
    width: 862px;
    margin: 0;
    text-align: center;
    font-size: 22px;
    letter-spacing: 0.1em;
    line-height: 42px;
  }
  .request { top: 424px; }
  .venue { top: 672px; }
  .details span { display: block; }
</style>
</head>
<body>
<main class="invitation">
  <svg class="window" viewBox="0 0 500 696" xmlns="http://www.w3.org/2000/svg" aria-hidden="false">
    <defs>
      <clipPath id="pane-area">
        <path d="M36,696 V232 A214,214 0 0 1 464,232 V696 Z"/>
      </clipPath>
    </defs>

    <path class="window-frame"
      d="M18,696 V232 A232,232 0 0 1 482,232 V696 Z M36,696 V232 A214,214 0 0 1 464,232 V696 Z"/>

    <g class="window-muntins" clip-path="url(#pane-area)">
      <path class="window-bar" d="M128,264 A122,122 0 0 1 372,264"/>
      <line class="window-bar" x1="250" y1="0" x2="250" y2="142"/>
      <line class="window-bar" x1="250" y1="264" x2="250" y2="696"/>
      <line class="window-bar" x1="134" y1="264" x2="134" y2="696"/>
      <line class="window-bar" x1="366" y1="264" x2="366" y2="696"/>
      <line class="window-bar" x1="0" y1="264" x2="500" y2="264"/>
      <line class="window-bar" x1="0" y1="353" x2="500" y2="353"/>
      <line class="window-bar" x1="0" y1="452" x2="500" y2="452"/>
      <line class="window-bar" x1="0" y1="549" x2="500" y2="549"/>
      <line class="window-bar" x1="137" y1="217" x2="-27" y2="149"/>
      <line class="window-bar" x1="184" y1="162" x2="87" y2="13"/>
      <line class="window-bar" x1="316" y1="162" x2="413" y2="13"/>
      <line class="window-bar" x1="363" y1="217" x2="527" y2="149"/>
    </g>

    <rect class="monogram-ornament" x="164" y="20" width="172" height="54" rx="3"
      role="img" aria-label="Scrollwork flourish border framing the monogram"/>
    <rect class="monogram-plaque" x="213" y="28" width="74" height="38"/>

    <rect class="skyline" x="36" y="648" width="428" height="48"
      role="img" aria-label="Washington DC skyline silhouette with monument and domes"/>
  </svg>

  <div class="monogram" aria-label="Monogram L and O">L&amp;O</div>

  <h1 class="couple">Lena &amp; Osmond</h1>

  <p class="details request">
    <span>Request the honour of your company</span>
    <span>on their wedding</span>
    <span>Saturday, the twelfth of April</span>
    <span>two thousand and fourteen</span>
    <span>at six in the evening</span>
  </p>

  <p class="details venue">
    <span>17th floor</span>
    <span>The Brightmoor Hall</span>
    <span>4200 Larkspur Crescent Dr</span>
    <span>Vienna, VA 22190</span>
    <span>United States</span>
  </p>
</main>
</body>
</html>
```